QBoost480 Business Card Design

I am in need of a business card design.

Business Name: Quantum Boost 480 or Qboost480 (we can try the business card with both variations)

I would like it to be somewhat different from the "average" business card

What do we do?

We link up with distributors of different items and we Market their products, sell their products, fulfill the shipment, and handle all customer service that goes along with it.

I will be uploading our logo as well as other business card ideas that i have seen and liked on the web.

I like the style of the "graphic design" business card that i uploaded. I was thinking maybe something like that but instead would read.

SYNC | SELL | SHIP

With maybe:
a computer or a Sync icon underneath SYNC
Some form of money sign underneath Sell
a delivery truck or something underneath SHIP.

And then I was thinking maybe put the logo on the back side like in the other business card that i uploaded.

I definitely want a double sided business card.

These are only my suggestions and if i was very confident in my idea then I wouldn't have to be on here. (So make what you think is nice because my opinion is probably not so great anyway!!)

Everything can be changed.

ALSO, For the logo
We can try and remove the text multi channel selling

For the Business card contact info:
Milo Quenton
CEO
2914 Ravensby Street
J7T-2K8
Montreal, Quebec

Thanks

Target Market(s)

Businesses

Industry/Entity Type

Information Technology

Font styles to use
Serif
Sans Serif
Decorative

Colors
34a6d6
33b8a4
aaaaaa
85cae6
33a6d7
0492cd
9d9d9d

Requirements
Must have
• Double Sided Business card
Nice to have
• Illustration graphics / Icons underneath the main points

```html
<!DOCTYPE html>
<html lang="en">
<head>
<meta charset="utf-8">
<title>QBoost480 Business Card</title>
<link href="https://fonts.googleapis.com/css2?family=Questrial&display=swap" rel="stylesheet">
<style>
  :root {
    --bg: #e7e4df;
    --ink-dark: #2b2c2e;
    --ink-darker: #222325;
    --paper: #f6f7f7;
    --blue: #34a6d6;
    --blue-deep: #0492cd;
    --blue-light: #85cae6;
    --lime: #a6cc3a;
    --grey: #9d9d9d;
    --grey-light: #d8d8d8;
    --white: #ffffff;
  }
  * { box-sizing: border-box; margin: 0; padding: 0; }
  html, body { width: 734px; height: 1200px; overflow: hidden; }
  body {
    background: var(--bg);
    font-family: "Questrial", sans-serif;
    position: relative;
  }
  .card {
    position: absolute;
    left: 57px;
    width: 620px;
    height: 354px;
    border-radius: 14px;
    overflow: hidden;
    box-shadow: 0 10px 24px rgba(0,0,0,.18);
  }
  .card--front { top: 150px; background: var(--ink-dark); }
  .card--back { top: 696px; background: var(--ink-dark); }

  /* Front */
  .front__panel {
    position: absolute; left: 0; top: 0; bottom: 0; width: 338px;
    background: var(--paper);
  }
  .front__divider { position: absolute; left: 320px; top: 0; height: 354px; width: 60px; }
  .brand {
    position: absolute;
    display: flex; align-items: center; gap: 12px;
    font-size: 42px; letter-spacing: .5px;
  }
  .front__brand { left: 50px; top: 150px; color: var(--blue); }
  .brand__dot { width: 16px; height: 16px; border-radius: 50%; background: var(--lime); }
  .contact { position: absolute; left: 400px; top: 62px; color: var(--grey-light); }
  .contact__name { font-size: 27px; color: var(--white); }
  .contact__role { font-size: 14px; color: var(--blue); margin-top: 2px; letter-spacing: 1px; }
  .contact__rule { width: 180px; height: 2px; background: var(--blue); margin: 12px 0 18px; }
  .contact__line { font-size: 14px; line-height: 27px; }

  /* Back */
  .back__edge { position: absolute; left: 0; top: 0; bottom: 0; width: 8px; background: var(--blue); }
  .back__panel {
    position: absolute; right: 0; top: 0; bottom: 0; width: 292px;
    background: linear-gradient(180deg, var(--blue-light) 0%, var(--blue) 45%, var(--blue-deep) 100%);
  }
  .back__brand { left: 52px; top: 140px; color: var(--grey-light); }
  .back__tagline {
    position: absolute; left: 54px; top: 196px;
    font-size: 13px; color: var(--grey-light); letter-spacing: 1px;
  }
  .pillars {
    position: absolute; right: 0; top: 118px; width: 292px;
    display: flex; justify-content: center; align-items: flex-end; gap: 8px;
  }
  .pillar { display: flex; flex-direction: column; align-items: center; gap: 12px; width: 74px; }
  .pillar__icon { width: 40px; height: 40px; }
  .pillar__label { font-size: 20px; color: var(--white); letter-spacing: 1px; }
  .pillars__sep { font-size: 20px; color: var(--white); padding-bottom: 1px; }
</style>
</head>
<body>

<section class="card card--front" aria-label="Business card, contact side">
  <div class="front__panel"></div>
  <svg class="front__divider" viewBox="0 0 60 354" aria-hidden="true">
    <rect x="14" y="0" width="6" height="354" fill="var(--lime)"/>
    <rect x="20" y="0" width="12" height="354" fill="var(--blue)"/>
    <path d="M32 40 h12 a6 6 0 0 1 6 6 v262 a6 6 0 0 1 -6 6 h-12 z" fill="var(--blue)"/>
    <circle cx="41" cy="80" r="7" fill="var(--lime)"/>
    <path d="M41 75 a3 3 0 1 1 0 6 a3 3 0 1 1 0 -6z" fill="var(--blue)"/>
    <rect x="34" y="240" width="14" height="10" rx="2" fill="var(--lime)"/>
    <rect x="34" y="270" width="14" height="10" rx="2" fill="var(--lime)"/>
  </svg>
  <div class="brand front__brand"><span class="brand__dot"></span>Qboost480</div>
  <div class="contact">
    <p class="contact__name">Milo Quenton</p>
    <p class="contact__role">CEO</p>
    <div class="contact__rule"></div>
    <p class="contact__line">2914 Ravensby Street</p>
    <p class="contact__line">J7T-2K8</p>
    <p class="contact__line">Montreal, Quebec</p>
    <p class="contact__line">000.000.0000</p>
    <p class="contact__line">hello@qboost480.com</p>
  </div>
</section>

<section class="card card--back" aria-label="Business card, brand side">
  <div class="back__edge"></div>
  <div class="brand back__brand"><span class="brand__dot"></span>Qboost480</div>
  <p class="back__tagline">Multi Channel Selling</p>
  <div class="back__panel"></div>
  <div class="pillars">
    <div class="pillar">
      <svg class="pillar__icon" viewBox="0 0 40 40" aria-hidden="true">
        <circle cx="20" cy="20" r="19" fill="var(--lime)"/>
        <rect x="10" y="11" width="20" height="13" rx="1.5" fill="none" stroke="var(--blue-deep)" stroke-width="2"/>
        <path d="M16 29 h8 M20 24 v5" stroke="var(--blue-deep)" stroke-width="2"/>
      </svg>
      <span class="pillar__label">SYNC</span>
    </div>
    <span class="pillars__sep">|</span>
    <div class="pillar">
      <svg class="pillar__icon" viewBox="0 0 40 40" aria-hidden="true">
        <circle cx="20" cy="20" r="19" fill="var(--lime)"/>
        <circle cx="20" cy="20" r="11" fill="none" stroke="var(--blue-deep)" stroke-width="2"/>
        <path d="M24 15.5 c-1-1.5-7-2-7 1.5 s7 2 7 5.5 s-6 3-7 1 M20 12.5 v15" fill="none" stroke="var(--blue-deep)" stroke-width="1.8"/>
      </svg>
      <span class="pillar__label">SELL</span>
    </div>
    <span class="pillars__sep">|</span>
    <div class="pillar">
      <svg class="pillar__icon" viewBox="0 0 40 40" aria-hidden="true">
        <circle cx="20" cy="20" r="19" fill="var(--lime)"/>
        <path d="M8 14 h15 v11 h-15 z M23 17 h5 l4 4 v4 h-9 z" fill="var(--blue-deep)"/>
        <circle cx="13" cy="27" r="2.5" fill="var(--blue-deep)" stroke="var(--lime)" stroke-width="1"/>
        <circle cx="28" cy="27" r="2.5" fill="var(--blue-deep)" stroke="var(--lime)" stroke-width="1"/>
      </svg>
      <span class="pillar__label">SHIP</span>
    </div>
  </div>
</section>

</body>
</html>
```